Website Design for Employee Moral and Happiness Company

Looking for a clean website design that explains our features in a step by step manner so our visitors know exactly what our site does before logging in.

The site is called "Velquo". See logo design and video for a sample of style and an overview of what we do.

Target Market(s)

Business owners that are looking to retain employees.

Number of Pages Required

1 page

```html
<!DOCTYPE html>
<html lang="en">
<head>
<meta charset="utf-8">
<title>Velquo – Event planning for happier teams</title>
<link href="https://fonts.googleapis.com/css2?family=Poppins:wght@400;500;600;700;800&display=swap" rel="stylesheet">
<style>
:root{
  --orange:#ff6a00;
  --orange-soft:#ffd9bf;
  --peach:#fde7da;
  --ink:#111111;
  --text:#444444;
  --muted:#8a8a8a;
  --grey-band:#f4f4f4;
  --white:#ffffff;
}
*{margin:0;padding:0;box-sizing:border-box}
html,body{width:1200px;height:3939px;overflow:hidden}
body{font-family:"Poppins",sans-serif;color:var(--ink);background:var(--white);position:relative}
.abs{position:absolute}
.brand{font-family:"Poppins",sans-serif;font-weight:700;color:var(--ink);letter-spacing:1px}
/* nav */
.nav-brand{left:88px;top:18px;font-size:40px}
.nav{left:430px;top:37px;display:flex;gap:30px;font-size:12px;font-weight:500;text-transform:uppercase}
.nav a{color:var(--ink);text-decoration:none}
.nav a.active{color:var(--orange)}
.login{left:1018px;top:28px;width:93px;height:36px;border-radius:18px;background:#e9e9e9;font-size:12px;font-weight:600;display:flex;align-items:center;justify-content:center;gap:6px}
/* buttons */
.btn{display:flex;align-items:center;justify-content:center;border-radius:24px;font-size:12px;font-weight:700;text-transform:uppercase}
.btn-orange{background:var(--orange);color:var(--white)}
.btn-white{background:var(--white);color:var(--ink)}
/* hero */
.hero-title{left:88px;top:200px;font-size:45px;font-weight:800;line-height:49px}
.hero-sub{left:88px;top:362px;font-size:16px;color:var(--text)}
.hero-btn{left:90px;top:410px;width:170px;height:42px}
.hero-art{left:545px;top:130px;width:585px;height:425px}
/* section labels */
.label{font-size:11px;font-weight:500;text-transform:uppercase;color:var(--ink);display:flex;align-items:center;gap:12px}
.label::before{content:"";width:36px;height:1px;background:#999}
.h2{font-size:38px;font-weight:800;line-height:44px}
.para{font-size:13.5px;line-height:23px;color:var(--text)}
/* about */
.about-photo{left:120px;top:610px;width:490px;height:365px}
.about-label{left:676px;top:657px}
.about-title{left:676px;top:678px}
.about-text{left:676px;top:737px;width:395px}
.read-more{left:675px;top:922px;font-size:12px;font-weight:700;text-decoration:underline;text-underline-offset:3px}
/* download */
.dl-label{left:185px;top:1135px}
.dl-title{left:185px;top:1157px}
.dl-text{left:185px;top:1261px;width:415px}
.store{height:52px;width:172px;border-radius:26px;background:var(--ink);color:var(--white);display:flex;align-items:center;gap:10px;padding-left:22px}
.store small{display:block;font-size:8px;text-transform:uppercase;line-height:10px}
.store b{display:block;font-size:15px;font-weight:600;line-height:18px}
.phone-screen-brand{font-size:34px;color:var(--ink)}
/* employee */
.card{background:var(--white);border-radius:6px;box-shadow:0 6px 24px rgba(0,0,0,.09);padding:6px;text-align:center}
.card .ph{border-radius:4px}
.card h4{font-size:15px;font-weight:700;margin-top:12px}
.card p{font-size:11px;color:var(--muted);margin-top:4px}
.emp-label{left:686px;top:1771px}
.emp-title{left:686px;top:1793px}
.emp-text{left:686px;top:1892px;width:395px}
/* raffles */
.raf-label{left:116px;top:2293px}
.raf-title{left:116px;top:2315px}
.raf-text{left:116px;top:2414px;width:390px}
.tag{background:var(--white);border-radius:10px;box-shadow:0 6px 20px rgba(0,0,0,.1);display:flex;flex-direction:column;align-items:center;justify-content:center;font-size:11px;font-weight:700;gap:4px}
/* events */
.events-title{left:0;width:1200px;top:2650px;text-align:center;font-size:38px;font-weight:800}
.event{width:276px;height:368px;background:var(--white);border-radius:6px;box-shadow:0 6px 24px rgba(0,0,0,.08);overflow:hidden}
.event .ph{height:205px}
.event .body{padding:20px 24px}
.event time{font-size:11px;color:var(--muted)}
.event h4{font-size:15px;font-weight:700;line-height:20px;margin-top:10px}
.event p{font-size:11.5px;line-height:19px;color:var(--text);margin-top:14px}
/* cta */
.cta{left:138px;top:3200px;width:924px;height:203px;border-radius:102px;background:var(--orange)}
.cta-text{left:245px;top:3262px;font-size:42px;font-weight:800;line-height:53px;color:var(--white)}
.cta-btn{left:770px;top:3280px;width:185px;height:42px}
/* footer */
.foot-brand{left:98px;top:3638px;font-size:56px;color:var(--white)}
.socials{left:118px;top:3732px;display:flex;gap:12px}
.socials span{width:40px;height:40px;border-radius:50%;background:#1d1d1d;display:block}
.foot-h{font-size:19px;font-weight:700;color:var(--white)}
.foot-list{list-style:none;font-size:12px;color:#dddddd;line-height:31px}
.foot-list li::before{content:"›";margin-right:8px}
.contact-item{display:flex;gap:10px;font-size:12px;color:#dddddd;line-height:17px;margin-bottom:22px}
.contact-item svg{flex:none;margin-top:2px}
.newsletter-note{font-size:12px;color:#dddddd;line-height:17px;width:250px}
.news-input{width:258px;height:46px;border-radius:23px;background:var(--white);display:flex;align-items:center;padding:0 18px;font-size:12px;color:#555;justify-content:space-between}
.bottom-line{left:88px;right:88px;top:3878px;height:1px;background:#2a2a2a}
.copyright{left:88px;top:3903px;font-size:12px;color:#dddddd}
.legal{right:90px;top:3903px;display:flex;gap:26px;font-size:12px;color:#dddddd}
.to-top{left:1132px;top:3860px;width:40px;height:40px;border-radius:50%;background:var(--orange);display:flex;align-items:center;justify-content:center}
</style>
</head>
<body>

<!-- header -->
<div class="abs nav-brand brand">velquo</div>
<nav class="abs nav">
  <a class="active" href="#">Home</a><a href="#">About us</a><a href="#">Employee</a><a href="#">Event planner</a><a href="#">From raffles</a><a href="#">Contact us</a>
</nav>
<div class="abs login">
  <svg width="10" height="10" viewBox="0 0 10 10"><circle cx="5" cy="3" r="2.5" fill="#111"/><path d="M0 10c0-3 2-4.5 5-4.5s5 1.5 5 4.5z" fill="#111"/></svg>LOGIN
</div>

<!-- hero -->
<h1 class="abs hero-title">Welcome to<br>velquo explainer<br>cutdown</h1>
<p class="abs hero-sub">Start building your event today with me!</p>
<div class="abs btn btn-orange hero-btn">My event planner</div>
<div class="abs hero-art" role="img" aria-label="Brand mascot illustration">
  <svg width="585" height="425" viewBox="0 0 585 425"><ellipse cx="292" cy="210" rx="280" ry="200" fill="#fff1e8"/><ellipse cx="292" cy="210" rx="200" ry="140" fill="#ffd9bf"/></svg>
</div>

<!-- grey band -->
<svg class="abs" style="left:0;top:920px" width="1200" height="603" viewBox="0 0 1200 603">
  <path d="M0 100 C120 -30 260 80 420 130 C620 190 820 230 1000 170 C1100 130 1170 60 1200 30 L1200 603 L0 603 Z" fill="#f4f4f4"/>
</svg>

<!-- about -->
<div class="abs about-photo" role="img" aria-label="Photo of a smiling team standing together in an office">
  <svg width="490" height="365" viewBox="0 0 490 365"><path d="M60 120 C120 20 260 -10 380 20 C470 45 500 150 440 250 C380 350 230 380 120 330 C20 290 0 200 60 120Z" fill="#ffd9bf"/><path d="M80 130 C140 40 270 10 380 40 C460 60 480 160 430 250 C370 340 230 360 140 320 C50 280 40 200 80 130Z" fill="#b9c2c9"/></svg>
</div>
<div class="abs label about-label">Introduction</div>
<h2 class="abs h2 about-title">About velquo</h2>
<p class="abs para about-text">Aenean sollicitudin, lorem quis bibendum auctor, nisi elit consequat ipsum, nec sagittis sem nibh id elit duis sed odio sit amet nibh vulputate cursus a sit amet mauris. Morbi accumsan ipsum velit. Nam nec tellus a odio tincidunt auctor a ornare odio. Sed non  mauris vitae erat consequat auctor eu in elit class aptent taciti sociosqu ad litora...</p>
<div class="abs read-more">READ MORE</div>

<!-- download -->
<div class="abs label dl-label">Download</div>
<h2 class="abs h2 dl-title">I am here to help<br>business like yours</h2>
<p class="abs para dl-text">Aenean sollicitudin, lorem quis bibendum auctor, nisi elit consequat ipsum, nec sagittis sem nibh elit duis sed odio sit amet nibh vulputate</p>
<div class="abs store" style="left:184px;top:1358px">
  <svg width="18" height="18" viewBox="0 0 18 18"><path d="M3 2 L15 9 L3 16 Z" fill="#ff6a00"/></svg>
  <div><small>Get in on</small><b>App Market</b></div>
</div>
<div class="abs store" style="left:366px;top:1358px">
  <svg width="18" height="18" viewBox="0 0 18 18"><circle cx="9" cy="9" r="7" fill="#fff"/></svg>
  <div><small>Download on the</small><b>Play Hub</b></div>
</div>
<svg class="abs" style="left:630px;top:1050px" width="400" height="610" viewBox="0 0 400 610">
  <circle cx="140" cy="140" r="130" fill="#ff6a00"/>
  <circle cx="295" cy="515" r="88" fill="#111"/>
  <rect x="98" y="100" width="217" height="445" rx="30" fill="#ff6a00"/>
  <rect x="103" y="105" width="207" height="435" rx="26" fill="#111"/>
  <rect x="112" y="114" width="189" height="417" rx="20" fill="#fff"/>
  <rect x="152" y="110" width="109" height="18" rx="8" fill="#111"/>
</svg>
<div class="abs phone-screen-brand brand" style="left:766px;top:1345px">velquo</div>

<!-- employee -->
<svg class="abs" style="left:150px;top:1590px" width="500" height="540" viewBox="0 0 500 540">
  <circle cx="330" cy="290" r="140" fill="#fde7da"/>
  <circle cx="78" cy="22" r="10" fill="#f7b84a"/>
  <circle cx="410" cy="93" r="5" fill="#8fc4f0"/>
  <circle cx="375" cy="523" r="8" fill="#7aa17a"/>
  <circle cx="34" cy="530" r="22" fill="#4bb8c0"/>
</svg>
<div class="abs card" style="left:133px;top:1645px;width:217px;height:258px">
  <div class="ph" role="img" aria-label="Portrait of a smiling team member" style="height:188px;background:#b9b2e6"></div>
  <h4>Marco Delain</h4><p>Event Planner</p>
</div>
<div class="abs card" style="left:374px;top:1745px;width:218px;height:280px">
  <div class="ph" role="img" aria-label="Portrait of a team member with crossed arms" style="height:206px;background:#8ec8e6"></div>
  <h4>Marco Delain</h4><p>Event Planner</p>
</div>
<div class="abs card" style="left:183px;top:1925px;width:165px;height:195px">
  <div class="ph" role="img" aria-label="Portrait of a surprised team member" style="height:126px;background:#f2a23a"></div>
  <h4>Marco Delain</h4><p>Event Planner</p>
</div>
<div class="abs label emp-label">Employee</div>
<h2 class="abs h2 emp-title">Increase employee<br>retention</h2>
<p class="abs para emp-text">Aenean sollicitudin, lorem quis bibendum auctor, nisi elit consequat ipsum, nec sagittis sem nibh id elit duis sed odio sit amet nibh vulputate...</p>

<!-- raffles -->
<div class="abs label raf-label">Raffles</div>
<h2 class="abs h2 raf-title">From raffles to<br>auctions</h2>
<p class="abs para raf-text">Aenean sollicitudin, lorem quis bibendum auctor, nisi elit consequat ipsum, nec sagittis sem nibh id elit duis sed odio sit amet nibh vulputate...</p>
<svg class="abs" style="left:610px;top:2080px" width="480" height="470" viewBox="0 0 480 470">
  <path d="M200 160 C250 80 370 60 440 110 C500 160 470 260 400 330 C330 400 230 450 130 440 C40 430 10 360 50 300 C90 240 160 230 200 160Z" fill="#ffd9bf"/>
  <path d="M190 170 C240 95 350 80 410 125 C465 170 440 265 375 330 C310 395 220 435 135 425 C55 415 30 355 65 300 C100 250 155 235 190 170Z" fill="#ff6a00"/>
</svg>
<div class="abs" role="img" aria-label="Photo of a smiling man in a denim shirt with arms crossed" style="left:700px;top:2085px;width:300px;height:455px;background:linear-gradient(180deg,#c8a38c 0%,#8eaad0 35%,#7d9cc6 100%);border-radius:140px 140px 40px 40px;opacity:.95"></div>
<div class="abs tag" style="left:548px;top:2300px;width:100px;height:90px;transform:rotate(-18deg)">
  <svg width="30" height="22" viewBox="0 0 30 22"><rect x="2" y="2" width="26" height="18" rx="3" fill="none" stroke="#111" stroke-width="2"/><line x1="10" y1="2" x2="10" y2="20" stroke="#111" stroke-width="2" stroke-dasharray="2 2"/></svg>TICKET
</div>
<div class="abs tag" style="left:672px;top:2500px;width:92px;height:92px;transform:rotate(-14deg)">
  <svg width="26" height="30" viewBox="0 0 26 30"><circle cx="13" cy="10" r="9" fill="none" stroke="#111" stroke-width="2"/><line x1="13" y1="19" x2="13" y2="29" stroke="#111" stroke-width="2"/></svg>BID
</div>

<!-- events -->
<h2 class="abs events-title">Velquo events</h2>
<article class="abs event" style="left:170px;top:2725px">
  <div class="ph" role="img" aria-label="Photo of two colleagues looking at a laptop" style="background:linear-gradient(135deg,#d9d4cc,#6d7480)"></div>
  <div class="body"><time>25-02-2022</time><h4>Some event heading<br>goes here</h4><p>Aenean sollicitudin lorem ipsum bibendum auctor nisi elit consequat ipsum...</p></div>
</article>
<article class="abs event" style="left:463px;top:2725px">
  <div class="ph" role="img" aria-label="Photo of a team shaking hands in a meeting" style="background:linear-gradient(135deg,#e6e2dc,#5b6a7c)"></div>
  <div class="body"><time>25-02-2022</time><h4>Some event heading<br>goes here</h4><p>Aenean sollicitudin lorem ipsum bibendum auctor nisi elit consequat ipsum...</p></div>
</article>
<article class="abs event" style="left:756px;top:2725px">
  <div class="ph" role="img" aria-label="Photo of a man working at a desk" style="background:linear-gradient(135deg,#f1f0ee,#8a96a4)"></div>
  <div class="body"><time>25-02-2022</time><h4>Some event heading<br>goes here</h4><p>Aenean sollicitudin lorem ipsum bibendum auctor nisi elit consequat ipsum...</p></div>
</article>

<!-- footer background -->
<svg class="abs" style="left:0;top:3290px" width="1200" height="649" viewBox="0 0 1200 649">
  <rect width="1200" height="649" fill="#111"/>
  <path d="M0 0 L1200 0 L1200 30 C1100 40 960 140 760 200 C560 240 280 235 120 170 C60 145 20 110 0 80 Z" fill="#fff"/>
</svg>

<!-- cta -->
<div class="abs cta"></div>
<div class="abs cta-text">Start building your<br>event today with me!</div>
<div class="abs btn btn-white cta-btn">My event planner</div>

<!-- footer -->
<div class="abs foot-brand brand">velquo</div>
<div class="abs socials"><span></span><span></span><span></span><span></span></div>

<div class="abs" style="left:419px;top:3582px">
  <div class="foot-h">Quick links</div>
  <ul class="foot-list" style="margin-top:14px">
    <li>Home</li><li>About Us</li><li>Employee</li><li>Event Planner</li><li>From Raffles</li><li>Contact Us</li>
  </ul>
</div>

<div class="abs" style="left:604px;top:3582px">
  <div class="foot-h">Contact info</div>
  <div style="margin-top:22px">
    <div class="contact-item"><svg width="12" height="10" viewBox="0 0 12 10"><rect x="0.5" y="0.5" width="11" height="9" fill="#ff6a00"/><path d="M0.5 0.5 L6 5 L11.5 0.5" stroke="#111" fill="none"/></svg><div>Email:<br>hello@velquo.example</div></div>
    <div class="contact-item"><svg width="12" height="12" viewBox="0 0 12 12"><path d="M2 1 L5 1 L6 4 L4 5 C5 7 6 8 8 8 L9 6 L12 7 L12 10 C12 11 11 12 10 12 C5 12 0 7 0 3 C0 2 1 1 2 1Z" fill="#ff6a00"/></svg><div>Phone:<br>+00 321 654 0987</div></div>
    <div class="contact-item"><svg width="10" height="13" viewBox="0 0 10 13"><path d="M5 0 C8 0 10 2 10 5 C10 8 5 13 5 13 C5 13 0 8 0 5 C0 2 2 0 5 0Z" fill="#ff6a00"/><circle cx="5" cy="5" r="2" fill="#111"/></svg><div>Location:<br>Some address line here<br>Northvale QX1 2AB</div></div>
  </div>
</div>

<div class="abs" style="left:852px;top:3584px">
  <div class="foot-h">Newsletter</div>
  <p class="newsletter-note" style="margin-top:20px">Subscribe to our email address to get the latest news.</p>
  <div class="news-input" style="margin-top:18px">
    <span>✉ Enter Your Email...</span>
    <svg width="16" height="16" viewBox="0 0 16 16"><path d="M0 7 L16 0 L11 16 L8 9 Z" fill="#ff6a00"/></svg>
  </div>
</div>

<div class="abs bottom-line"></div>
<div class="abs copyright">© Copyright 2022 velquo. All Rights Reserved</div>
<div class="abs legal"><span>Imprint</span><span>Privacy policy</span><span>Terms and Condition</span></div>
<div class="abs to-top"><svg width="12" height="14" viewBox="0 0 12 14"><path d="M6 1 L6 13 M1 6 L6 1 L11 6" stroke="#fff" stroke-width="1.6" fill="none"/></svg></div>

</body>
</html>
```